Theme and starter template for small business powerpoint deck

We are starting a technology consulting company and would like to have a powerpoint/google slide theme and initial template. We are more concerned with the theme/colors at this point. Initial template can be pretty simple. We would want a cover slide, agenda slide, some content slides including text content, image content, a combination of both, etc. A closing slide. we have included jpg files of our logo, let us know if you would prefer eps/vector. I assume you may want exact color data as well?

Target Market(s)

Technology and Customer Experience Leadership at companies with 25 or more employees

Industry/Entity Type

Technology Consulting

Font styles to use
Sans Serif

Colors
0054AA
0677BA
7BADD7
CADEEF
E8F1F8

Requirements
Must have
• I have attached JPG and EPS and vector files to project. I would like to stay with those colors but open to slight variation if recommended.

```html
<!DOCTYPE html>
<html lang="en">
<head>
<meta charset="utf-8">
<title>Verantis – Presentation Theme Overview</title>
<link href="https://fonts.googleapis.com/css2?family=Ubuntu:wght@500;700&family=Open+Sans:wght@400;600;700&display=swap" rel="stylesheet">
<style>
:root{
  --blue-deep:#0054AA;
  --blue-mid:#0677BA;
  --blue-light:#7BADD7;
  --blue-pale:#CADEEF;
  --blue-wash:#E8F1F8;
  --navy:#0B2F5C;
  --ink:#1E1E22;
  --text:#4A4A4F;
  --grey:#9A9AA0;
  --page:#FFFFFF;
}
*{margin:0;padding:0;box-sizing:border-box}
html,body{width:1200px;height:1065px;overflow:hidden;background:var(--page)}
body{position:relative;font-family:"Open Sans",sans-serif;color:var(--text)}
.slide-frame{position:absolute;width:349px;height:196px;box-shadow:0 4px 14px rgba(0,0,0,.18)}
.slide{position:absolute;left:0;top:0;width:596px;height:335px;transform:scale(.5856);transform-origin:0 0;background:#fff;overflow:hidden;border:1px solid var(--blue-pale)}
.abs{position:absolute}
.brand{position:absolute;right:8px;top:8px;font-family:"Ubuntu",sans-serif;font-weight:700;font-size:16px;letter-spacing:.5px;color:var(--ink);display:flex;align-items:center;gap:4px;border-bottom:1.5px solid var(--grey);padding-bottom:1px}
.brand i{display:block;width:8px;height:8px;background:var(--blue-mid)}
.title{position:absolute;font-family:"Ubuntu",sans-serif;font-weight:500;font-size:17px;color:var(--ink);padding-left:11px;border-left:1.5px solid var(--grey);line-height:20px;white-space:nowrap}
.body{font-size:7.6px;line-height:13.2px;color:var(--text);text-align:justify}
.center{text-align:center}
.foot-url{position:absolute;left:0;bottom:6px;width:130px;height:19px;background:var(--blue-deep);color:#fff;font-size:6.5px;display:flex;align-items:center;gap:5px;padding-left:8px;white-space:nowrap}
.foot-url b{width:12px;height:12px;border-radius:50%;border:1.5px solid #fff;display:block;flex:none}
.foot-copy{position:absolute;left:0;right:0;bottom:11px;text-align:center;font-size:6.5px;color:var(--text)}
.foot-page{position:absolute;right:0;bottom:6px;width:38px;height:19px;background:var(--blue-mid);color:#fff;font-size:6.5px;display:flex;align-items:center;justify-content:center}
/* agenda */
.pill{position:absolute;width:214px;height:27px;border-radius:8px 0 8px 0;color:#fff;font-size:7.5px;display:flex;justify-content:space-between;align-items:center;padding:0 16px;box-shadow:0 2px 3px rgba(0,0,0,.2)}
.pill.deep{background:var(--blue-deep)}
.pill.mid{background:var(--blue-mid)}
/* what we do */
.item{position:absolute;width:150px;border-left:1px solid var(--blue-pale);padding-left:9px}
.item .num{position:absolute;left:9px;top:0;font-family:"Ubuntu",sans-serif;font-weight:500;font-size:19px;color:var(--blue-mid)}
.item h4{margin-left:20px;font-size:6.8px;font-weight:700;color:var(--ink);line-height:8.5px;min-height:22px;padding-top:3px}
.item p{font-size:5.6px;line-height:9.6px;text-align:justify;color:var(--text)}
/* process */
.step h5{font-size:7.6px;font-weight:700;color:var(--ink);line-height:10.5px}
.step p{font-size:5.6px;line-height:7.6px;color:var(--text)}
/* history */
.hist{position:absolute;left:56px;width:490px;font-size:7.6px;line-height:12.8px;color:var(--text)}
.hist li{list-style:none;position:relative;padding-left:11px;margin-bottom:6.9px}
.hist li::before{content:"";position:absolute;left:0;top:4px;width:5px;height:5px;border-radius:50%;background:var(--blue-mid)}
/* contact */
.contact{display:flex;align-items:center;gap:10px;margin-bottom:8px}
.contact svg{flex:none}
.contact small{display:block;font-size:6px;color:var(--grey)}
.contact span{font-size:7.6px;color:var(--ink);white-space:nowrap}
</style>
</head>
<body>

<!-- Cover -->
<div class="slide-frame" style="left:33px;top:52px">
<section class="slide" style="background:linear-gradient(100deg,#EEF3F9 0%,#E8F1F8 45%,#F0F3F7 100%)">
  <svg class="abs" style="left:0;top:0" width="596" height="335" role="img" aria-label="Faint office photograph in the background">
    <polygon points="140,40 330,335 0,335" fill="#DCE8F4" opacity=".6"/>
    <polygon points="320,20 520,335 240,335" fill="#E2E8EF" opacity=".6"/>
  </svg>
  <div class="abs" style="left:18px;top:88px;font-family:'Ubuntu',sans-serif;font-weight:700;font-size:36px;color:var(--ink);letter-spacing:1px;border-bottom:2.5px solid var(--grey);line-height:40px;display:flex;align-items:center;gap:6px">VERANTIS<i style="display:block;width:20px;height:20px;background:var(--blue-mid)"></i></div>
  <div class="abs" style="left:18px;top:146px;font-family:'Ubuntu',sans-serif;font-weight:500;font-size:20px;line-height:27px;color:#3A3A40">Strategic Insights.<br>Proven Success</div>
  <div class="abs" style="left:20px;top:247px;font-size:8px;line-height:21px;color:var(--ink)">
    <div style="display:flex;align-items:center;gap:6px"><b style="width:12px;height:12px;border-radius:50%;background:var(--blue-deep)"></b>www.verantis-consult.com</div>
    <div style="display:flex;align-items:center;gap:6px"><b style="width:12px;height:12px;border-radius:50%;background:var(--blue-deep)"></b>hello@verantis-consult.com</div>
    <div style="display:flex;align-items:center;gap:6px"><b style="width:12px;height:12px;border-radius:50%;background:var(--blue-deep)"></b>+1 555 014 2290</div>
  </div>
  <svg class="abs" style="left:355px;top:70px" width="225" height="195" role="img" aria-label="Triangle collage of three business photographs">
    <polygon points="112,2 166,96 58,96" fill="#0054AA"/>
    <polygon points="56,100 110,190 0,190" fill="#7E8A98"/>
    <polygon points="168,100 222,190 114,190" fill="#0677BA"/>
    <polygon points="112,100 166,190 58,190" fill="#CADEEF" opacity=".8"/>
  </svg>
</section></div>

<!-- Agenda -->
<div class="slide-frame" style="left:424px;top:52px">
<section class="slide">
  <div class="brand">VERANTIS<i></i></div>
  <div class="title" style="left:264px;top:20px">Agenda</div>
  <div class="pill deep" style="left:72px;top:59px"><span>01. Agenda</span><span>01</span></div>
  <div class="pill mid" style="left:310px;top:59px"><span>02. About Us</span><span>02</span></div>
  <div class="pill mid" style="left:72px;top:98px"><span>02. Mission &amp; Vision</span><span>03</span></div>
  <div class="pill deep" style="left:310px;top:98px"><span>04. What We Do</span><span>04</span></div>
  <div class="pill deep" style="left:72px;top:137px"><span>03. Our Statistics</span><span>05</span></div>
  <div class="pill mid" style="left:310px;top:137px"><span>06. Our Process</span><span>06</span></div>
  <div class="pill mid" style="left:72px;top:176px"><span>04. Page Break</span><span>07</span></div>
  <div class="pill deep" style="left:310px;top:176px"><span>08. Our History</span><span>08</span></div>
  <div class="pill deep" style="left:72px;top:215px"><span>05. Perspiciatis Unde</span><span>09</span></div>
  <div class="pill mid" style="left:310px;top:215px"><span>10. Our Goals</span><span>10</span></div>
  <div class="pill mid" style="left:72px;top:254px"><span>06. What We Achieve</span><span>11</span></div>
  <div class="pill deep" style="left:310px;top:254px"><span>12. Ending</span><span>12</span></div>
  <div class="foot-url"><b></b>www.verantis-consult.com</div>
  <div class="foot-copy">© 2024. ALL Rights Reserved.</div>
  <div class="foot-page">Page 02</div>
</section></div>

<!-- About -->
<div class="slide-frame" style="left:815px;top:52px">
<section class="slide">
  <div class="brand">VERANTIS<i></i></div>
  <svg class="abs" style="left:60px;top:68px" width="212" height="186" role="img" aria-label="Photograph of two colleagues reviewing documents, in a triangle frame">
    <polygon points="106,3 208,183 4,183" fill="#C9B7A8" stroke="#0054AA" stroke-width="3"/>
  </svg>
  <div class="title" style="left:318px;top:117px">About Us</div>
  <p class="body abs" style="left:318px;top:145px;width:216px">Omnis isasdte natus errorsit voluseptatem accusantium doloremque laudantium, totasem rsem aperiam, eaque ipsa quae seab illo inventore veritatis et quasi architecto beatae vitae dicta sunt explicabo. Nemo enim ipsam voluptatem quia voluptas sit aspernatur aut odit.</p>
  <div class="foot-url"><b></b>www.verantis-consult.com</div>
  <div class="foot-copy">© 2024. ALL Rights Reserved.</div>
  <div class="foot-page">Page 03</div>
</section></div>

<!-- Vision -->
<div class="slide-frame" style="left:33px;top:306px">
<section class="slide">
  <div class="brand">VERANTIS<i></i></div>
  <svg class="abs" style="left:38px;top:30px" width="250" height="290" role="img" aria-label="Hexagon collage of team meeting photographs">
    <polygon points="32,4 60,20 60,52 32,68 4,52 4,20" fill="#5C8EBA"/>
    <polygon points="66,58 94,74 94,106 66,122 38,106 38,74" fill="#7BADD7"/>
    <polygon points="155,6 210,38 210,102 155,134 100,102 100,38" fill="#D9D3CF"/>
    <polygon points="95,120 160,158 160,234 95,272 30,234 30,158" fill="#5C5A60"/>
    <polygon points="200,128 242,152 242,200 200,224 158,200 158,152" fill="#3E7EB6"/>
    <polygon points="178,218 196,228 196,248 178,258 160,248 160,228" fill="#0677BA"/>
    <polygon points="166,256 186,268 186,292 166,302 146,292 146,268" fill="#A38D7A"/>
  </svg>
  <div class="title" style="left:333px;top:72px">Our Vision &amp; Mission</div>
  <p class="body abs" style="left:333px;top:101px;width:216px">Omnis isasdte natus errorsit voluseptatem accusantium doloremque laudantium, totasem rsem aperiam, eaque ipsa quae seab illo inventore veritatis et quasi architecto beatae vitae dicta sunt explicabo. Nemo enim ipsam voluptatem quia voluptas sit aspernatur aut odit.</p>
  <p class="body abs" style="left:333px;top:176px;width:216px">Kasedte natasesus errorsit voluseptatem accusantium doloremque laudantium, totasem rsem aperiam, eaque ipsa quae seab illo inventore veritatis et quasi architecto beatae vitae dicsaeta sunt explicabo. Nemo enim ipsam voluptatem quia voluptas sit aspernatur aut odit.</p>
  <div class="foot-url"><b></b>www.verantis-consult.com</div>
  <div class="foot-copy">© 2024. ALL Rights Reserved.</div>
  <div class="foot-page">Page 04</div>
</section></div>

<!-- What We Do -->
<div class="slide-frame" style="left:424px;top:306px">
<section class="slide">
  <div class="brand">VERANTIS<i></i></div>
  <div class="title" style="left:245px;top:30px">What We Do</div>
  <p class="body center abs" style="left:78px;top:60px;width:450px">Omnis isasdte natus errorsit voluseptatem accusantium doloremque laudantium, totasem rsem aperiam, eaque ipsa quae seab illo inventore veritatis et quasi architecto beatae vitae dicta sunt explicabo. Nemo enim ipsam voluptatem quia voluptas sit aspernatur aut odit.</p>
  <div class="item" style="left:47px;top:126px"><span class="num">1.</span><h4>VOLUPTATEM ACCUSANTIUM DOLOREMQUE LAUD.</h4><p>Werspiciatis aseeunde omnis iste natus error sitvolasuptate masease accusantium dolorem quelaudtium, totam rem aperiam.</p></div>
  <div class="item" style="left:230px;top:126px"><span class="num">2.</span><h4>VOLUPTATEM ACCUSANTIUM DOLOREMQUE LAUD.</h4><p>Werspiciatis aseeunde omnis iste natus error sitvolasuptate masease accusantium dolorem quelaudtium, totam rem aperiam.</p></div>
  <div class="item" style="left:412px;top:126px"><span class="num">3.</span><h4>VOLUPTATEM ACCUSANTIUM DOLOREMQUE LAUD.</h4><p>Werspiciatis aseeunde omnis iste natus error sitvolasuptate masease accusantium dolorem quelaudtium, totam rem aperiam.</p></div>
  <div class="item" style="left:47px;top:211px"><span class="num">4.</span><h4>VOLUPTATEM ACCUSANTIUM DOLOREMQUE LAUD.</h4><p>Werspiciatis aseeunde omnis iste natus error sitvolasuptate masease accusantium dolorem quelaudtium, totam rem aperiam.</p></div>
  <div class="item" style="left:230px;top:211px"><span class="num">5.</span><h4>VOLUPTATEM ACCUSANTIUM DOLOREMQUE LAUD.</h4><p>Werspiciatis aseeunde omnis iste natus error sitvolasuptate masease accusantium dolorem quelaudtium, totam rem aperiam.</p></div>
  <div class="item" style="left:412px;top:211px"><span class="num">6.</span><h4>VOLUPTATEM ACCUSANTIUM DOLOREMQUE LAUD.</h4><p>Werspiciatis aseeunde omnis iste natus error sitvolasuptate masease accusantium dolorem quelaudtium, totam rem aperiam.</p></div>
  <div class="foot-url"><b></b>www.verantis-consult.com</div>
  <div class="foot-copy">© 2024. ALL Rights Reserved.</div>
  <div class="foot-page">Page 05</div>
</section></div>

<!-- Statistics -->
<div class="slide-frame" style="left:815px;top:306px">
<section class="slide">
  <div class="brand">VERANTIS<i></i></div>
  <div class="title" style="left:240px;top:49px">Our Statistics</div>
  <p class="body center abs" style="left:68px;top:80px;width:460px">Omnis isasdte natus errorsit voluseptatem accusantium doloremque laudantium, totasem rsem aperiam, eaque ipsa quae seab illo inventore veritatis et quasi architecto beatae vitae dicta sunt explicabo.</p>
  <svg class="abs" style="left:130px;top:128px" width="330" height="134" font-family="Open Sans, sans-serif" font-size="6.5" font-weight="600" fill="#222">
    <g stroke="#E3E7EC" stroke-width="1" fill="none">
      <rect x="43" y="6" width="270" height="102" fill="#FBFCFD"/>
      <rect x="73" y="6" width="30" height="102" fill="#F1F5F9" stroke="none"/>
      <rect x="133" y="6" width="30" height="102" fill="#F1F5F9" stroke="none"/>
      <rect x="193" y="6" width="30" height="102" fill="#F1F5F9" stroke="none"/>
      <rect x="253" y="6" width="30" height="102" fill="#F1F5F9" stroke="none"/>
      <path d="M43 23H313M43 40H313M43 57H313M43 74H313M43 91H313M73 6V108M103 6V108M133 6V108M163 6V108M193 6V108M223 6V108M253 6V108M283 6V108"/>
    </g>
    <g text-anchor="end"><text x="18" y="12">70</text><text x="18" y="29">60</text><text x="18" y="46">50</text><text x="18" y="63">40</text><text x="18" y="80">30</text><text x="18" y="97">20</text><text x="18" y="114">10</text></g>
    <g text-anchor="middle"><text x="55" y="130">1/15</text><text x="93" y="130">1/15</text><text x="135" y="130">1/15</text><text x="175" y="130">1/15</text><text x="215" y="130">1/15</text><text x="255" y="130">1/15</text><text x="296" y="130">1/15</text></g>
    <g fill="none" stroke-width="2.2" stroke-linejoin="round">
      <polyline points="72,93 102,75 132,84 162,65" stroke="#0B2F5C"/>
      <polyline points="162,65 192,59 222,63 252,41" stroke="#7BADD7"/>
      <polyline points="252,41 282,41 307,23" stroke="#0677BA"/>
    </g>
  </svg>
  <div class="foot-url"><b></b>www.verantis-consult.com</div>
  <div class="foot-copy">© 2024. ALL Rights Reserved.</div>
  <div class="foot-page">Page 06</div>
</section></div>

<!-- Process -->
<div class="slide-frame" style="left:33px;top:561px">
<section class="slide">
  <div class="brand">VERANTIS<i></i></div>
  <div class="title" style="left:246px;top:19px">Our Process</div>
  <svg class="abs" style="left:190px;top:70px" width="220" height="184">
    <path d="M36 10 A100 100 0 1 0 180 10" fill="none" stroke="#BFC4CA" stroke-width="1"/>
    <circle cx="108" cy="76" r="66" fill="none" stroke="#CFD3D8" stroke-width="1"/>
    <circle cx="108" cy="76" r="61" fill="#0054AA"/>
    <g fill="#fff" stroke="#0677BA" stroke-width="1.2">
      <circle cx="36" cy="10" r="4.5"/><circle cx="180" cy="10" r="4.5"/>
      <circle cx="16" cy="114" r="4.5"/><circle cx="201" cy="114" r="4.5"/>
      <circle cx="110" cy="178" r="4.5"/>
    </g>
  </svg>
  <div class="abs" style="left:247px;top:137px;width:105px;text-align:center;font-family:'Ubuntu',sans-serif;font-weight:700;font-size:15px;color:#fff;letter-spacing:.5px">VERANTIS</div>
  <div class="step abs" style="left:18px;top:69px;width:190px;text-align:right"><h5>Faerspiciatis unde omnis iste natus error<br>sit voluptatem</h5><p style="text-align:center">Werspiciatis aseeunde omnis iste natus error sitvolasuptate masease accusantium dolorem quelaudtium, totam rem aperiam.</p></div>
  <div class="step abs" style="left:390px;top:69px;width:190px"><h5>Faerspiciatis unde omnis iste natus error<br>sit voluptatem</h5><p style="padding-left:16px">Werspiciatis aseeunde omnis iste natus error sitvolasuptate masease accusantium dolorem quelaudtium, totam rem aperiam.</p></div>
  <div class="step abs" style="left:18px;top:175px;width:175px;text-align:right"><h5>Faerspiciatis unde omnis iste natus error<br>sit voluptatem</h5><p style="text-align:center">Werspiciatis aseeunde omnis iste natus error sitvolasuptate masease accusantium dolorem quelaudtium, totam rem aperiam.</p></div>
  <div class="step abs" style="left:401px;top:175px;width:180px"><h5>Faerspiciatis unde omnis iste natus error<br>sit voluptatem</h5><p style="padding-left:8px">Werspiciatis aseeunde omnis iste natus error sitvolasuptate masease accusantium dolorem quelaudtium, totam rem aperiam.</p></div>
  <div class="step abs center" style="left:170px;top:259px;width:260px"><h5>Faerspiciatis unde omnis iste natus error<br>sit voluptatem</h5><p>Werspiciatis aseeunde omnis iste natus error sitvolasuptate masease accusantium dolorem quelaudtium, totam rem aperiam.</p></div>
  <div class="foot-url"><b></b>www.verantis-consult.com</div>
  <div class="foot-copy">© 2024. ALL Rights Reserved.</div>
  <div class="foot-page">Page 07</div>
</section></div>

<!-- Section break -->
<div class="slide-frame" style="left:424px;top:561px">
<section class="slide" style="border:none">
  <div class="abs" style="inset:0;background:linear-gradient(180deg,#0677BA 0%,#0060AE 55%,#0054AA 100%)" role="img" aria-label="Photograph of a team working in an office with a city skyline, tinted blue"></div>
  <div class="abs" style="left:38px;top:130px;font-family:'Ubuntu',sans-serif;font-weight:700;font-size:24px;color:#fff;padding-left:10px;border-left:1.5px solid #fff;line-height:26px;white-space:nowrap">Transforming Ideas into Results</div>
  <p class="abs" style="left:38px;top:168px;width:240px;font-size:9.5px;line-height:13px;color:#fff">Werspiciatis aseeunde omnis iste natus error sitvolasuptate masease.</p>
</section></div>

<!-- History -->
<div class="slide-frame" style="left:815px;top:561px">
<section class="slide">
  <div class="brand">VERANTIS<i></i></div>
  <div class="title" style="left:246px;top:19px">Our History</div>
  <ul class="hist" style="top:63px">
    <li>Harspiciatis unde omnis iste natus error sit voluptatem accusantium doloremque laudantium, totam rem aperiam, eaque ipsa quae ab illo inventore veritatis et quasi architecto beatae vitae dicta sunt explicabo. Nemo enim ipsam voluptatem quia voluptas sitsesee aspernatur aut odit</li>
    <li>Harspiciatis unde omnis iste natus error sit voluptatem accusantium doloremque laudantium, totam rem aperiam, eaque ipsa quae ab illo inventore veritatis et quasi architecto beatae vitae dicta sunt explicabo. Nemo enim ipsam voluptatem quia voluptas sitsesee aspernatur aut odit</li>
    <li>Harspiciatis unde omnis iste natus error sit voluptatem accusantium doloremque laudantium, totam rem aperiam, eaque ipsa quae ab illo inventore veritatis et quasi architecto beatae vitae dicta sunt explicabo. Nemo enim ipsam voluptatem quia voluptas sitsesee aspernatur aut odit</li>
    <li>Harspiciatis unde omnis iste natus error sit voluptatem accusantium doloremque laudantium, totam rem aperiam, eaque ipsa quae ab illo inventore veritatis et quasi architecto beatae vitae dicta sunt explicabo. Nemo enim ipsam voluptatem quia voluptas sitsesee aspernatur aut odit</li>
    <li>Harspiciatis unde omnis iste natus error sit voluptatem accusantium doloremque laudantium, totam rem aperiam, eaque ipsa quae ab illo inventore veritatis et quasi architecto beatae vitae dicta sunt explicabo. Nemo enim ipsam voluptatem quia voluptas sitsesee aspernatur aut odit</li>
  </ul>
  <div class="foot-url"><b></b>www.verantis-consult.com</div>
  <div class="foot-copy">© 2024. ALL Rights Reserved.</div>
  <div class="foot-page">Page 09</div>
</section></div>

<!-- Closing -->
<div class="slide-frame" style="left:424px;top:815px">
<section class="slide" style="background:#fff">
  <div class="abs" style="left:16px;top:8px;width:564px;height:5px;background:var(--blue-mid)"></div>
  <div class="abs" style="left:16px;top:322px;width:564px;height:5px;background:var(--blue-deep)"></div>
  <svg class="abs" style="left:0;top:14px" width="596" height="306">
    <polygon points="0,0 220,0 0,240" fill="#E8F1F8"/>
    <polygon points="220,0 596,0 596,14 380,306" fill="#E8F1F8"/>
    <polygon points="596,10 596,306 410,306" fill="#F2F7FB"/>
    <polygon points="192,18 348,292 32,292" fill="#CADEEF"/>
  </svg>
  <svg class="abs" style="left:84px;top:94px" width="220" height="184" role="img" aria-label="Triangle collage of a smiling consultant and two office photographs">
    <polygon points="108,2 162,92 54,92" fill="#0054AA"/>
    <polygon points="54,94 108,184 0,184" fill="#7E8A98"/>
    <polygon points="162,94 216,184 108,184" fill="#0677BA"/>
  </svg>
  <div class="abs" style="left:339px;top:92px;font-family:'Ubuntu',sans-serif;font-weight:700;font-size:27px;color:var(--ink);letter-spacing:1px;border-bottom:2px solid var(--grey);line-height:31px;display:flex;align-items:center;gap:5px">VERANTIS<i style="display:block;width:14px;height:14px;background:var(--blue-mid)"></i></div>
  <div class="abs" style="left:339px;top:150px">
    <div class="contact"><svg width="18" height="18"><circle cx="9" cy="9" r="8" fill="none" stroke="#0054AA" stroke-width="1.2"/><path d="M6 5.5l2 0 1 2.2-1.2.9a6 6 0 0 0 2.6 2.6l.9-1.2 2.2 1v2c-4 .3-7.8-3.5-7.5-7.5z" fill="#0054AA"/></svg><div><small>Call Us</small><span>+1 555 014 2290</span></div></div>
    <div class="contact"><svg width="18" height="18"><circle cx="9" cy="9" r="8" fill="none" stroke="#0054AA" stroke-width="1.2"/><rect x="5" y="6" width="8" height="6" fill="#0054AA"/><path d="M5 6l4 3.2L13 6" fill="none" stroke="#fff" stroke-width=".8"/></svg><div><small>Email</small><span>hello@verantis-consult.com</span></div></div>
    <div class="contact"><svg width="18" height="18"><circle cx="9" cy="9" r="8" fill="none" stroke="#0054AA" stroke-width="1.2"/><path d="M9 13.5s-3.2-3.3-3.2-5.5a3.2 3.2 0 0 1 6.4 0c0 2.2-3.2 5.5-3.2 5.5z" fill="#0054AA"/><circle cx="9" cy="8" r="1.1" fill="#fff"/></svg><div><small>Address</small><span>1420 Harbor Lane, Los Angeles, CA 90017</span></div></div>
  </div>
</section></div>

</body>
</html>
```